oloperra Web Design Project

It is a virtual assistance/concierge company that helps the busy professional by remotely providing administrative, technical and/or creative business support services, specializing in the medical device industry. Company name is oloperra.
(website will be oloperra.example)

Allowing things to be done without taking time away from more urgent issues or family/personal time. Partnering with a VA reduces stress, protects cash flow, eliminates administrative hassles, and enables business people to find the success they originally set out to achieve. Saves small businesses and/or individuals on overhead, salary, et. Work is done remotely to offer administrative, clerical, typing and specialist service assistance on a regular, ad-hoc or emergency cover basis.

Though we are capable of addressing the needs of medical professionals and industry representatives due to our experience and knowledge (sales, HCC guidelines, etc.) we do not want to be limited to that market only.

Target Market(s)

Target market would be M/F, 30-50, National, busy, Alpha, entrepreneurs and industry professionals who want/need to do more without sacrifice of life

Industry/Entity Type

Industry

Requirements
Nice to have
• We do have a logo designed via the MakerFolk website that can/should be included. Logo is uploaded.

```html
<!DOCTYPE html>
<html lang="en">
<head>
<meta charset="utf-8">
<title>oloperra – Virtual Assistance</title>
<link rel="stylesheet" href="https://fonts.googleapis.com/css2?family=Montserrat:wght@400;500;600;700&family=Arimo:ital,wght@0,400;0,700;1,400&display=swap">
<style>
:root{
  --navy:#1b3a63;
  --navy-dark:#0f2745;
  --navy-light:#2f5a8e;
  --red:#c40f12;
  --ink:#222;
  --muted:#444;
  --header-bg:#e9e9e9;
  --band:#cfcfcf;
  --page-bg:#f2f2f2;
  --panel-border:#d6d6d6;
  --white:#fff;
}
*{box-sizing:border-box;margin:0;padding:0}
html,body{width:1200px;height:1000px;overflow:hidden}
body{position:relative;background:var(--page-bg);font-family:"Arimo",Arial,sans-serif;color:var(--ink)}
.abs{position:absolute}

/* header */
.site-header{left:0;top:0;width:1200px;height:78px;background:var(--header-bg);border-bottom:6px solid var(--band);height:84px}
.brand{left:122px;top:22px;display:flex;align-items:center;gap:6px;font-family:"Montserrat",sans-serif;font-weight:600;font-size:28px;color:var(--navy-dark);letter-spacing:-.5px}
.brand .dot{width:14px;height:14px;border-radius:50%;background:var(--red)}
.main-nav{right:104px;top:29px;display:flex;gap:0;font-family:"Montserrat",sans-serif;font-size:14px}
.main-nav a{color:#222;text-decoration:none;padding:6px 21px;border-radius:4px}
.main-nav a.active{background:linear-gradient(#2d5386,var(--navy-dark));color:#fff;margin-right:2px}

/* hero */
.hero{left:0;top:84px;width:1200px;height:354px;background:radial-gradient(ellipse at 75% 30%,#3f6ea6 0%,#1f4b80 45%,#123561 100%);overflow:hidden}
.hero-photo{left:110px;top:85px;width:240px;height:270px;background:linear-gradient(#2b2b2b,#111);border-radius:110px 110px 0 0}
.hero-laptop{left:375px;top:55px;width:270px;height:200px;background:linear-gradient(160deg,#c9ccd2,#7d828b);border-radius:8px}
.hero-title{left:606px;top:48px;font-family:"Montserrat",sans-serif;font-size:35px;color:#fff;font-weight:400}
.hero-sub{right:158px;top:104px;font-family:"Montserrat",sans-serif;font-size:17px;color:#fff;text-align:right;line-height:24px}
.btn{display:inline-block;font-family:"Montserrat",sans-serif;font-size:14px;color:#fff;text-align:center;border-radius:6px;border:2px solid #a9b7c8}
.btn-try{left:866px;top:171px;width:83px;height:32px;line-height:28px;background:linear-gradient(#355c8f,var(--navy-dark))}
.btn-buy{left:962px;top:171px;width:83px;height:32px;line-height:28px;background:linear-gradient(#d8171a,#8e0608)}
.service-tabs{left:436px;top:306px;width:658px;height:48px;display:flex}
.service-tabs div{flex:1;display:flex;align-items:center;justify-content:center;font-family:"Arimo",sans-serif;font-weight:700;font-size:14px;background:linear-gradient(#fff,#e4e4e4);color:var(--navy-dark)}
.service-tabs div:first-child{border-radius:10px 0 0 0;flex:0 0 231px}
.service-tabs div:last-child{border-radius:0 10px 0 0;flex:0 0 216px}
.service-tabs div.active{background:var(--navy);color:#fff;position:relative}
.service-tabs div.active::before{content:"";position:absolute;top:-8px;left:50%;margin-left:-9px;border:9px solid transparent;border-top:0;border-bottom:8px solid var(--navy)}
.hero-band{left:0;top:438px;width:1200px;height:5px;background:var(--band)}

/* panels */
.panel{background:var(--white);border:1px solid var(--panel-border);box-shadow:0 0 0 8px #ececec inset}
.panel-main{left:114px;top:457px;width:643px;height:465px}
.panel-contact{left:773px;top:457px;width:321px;height:465px}
.heading{font-family:"Montserrat",sans-serif;font-weight:700;color:var(--navy);font-size:18px}
.heading em{color:var(--red);font-style:italic}
.help-title{left:150px;top:485px}
.social{left:528px;top:485px;display:flex;gap:5px;font-size:11px}
.social span{border:1px solid #bbb;border-radius:3px;padding:2px 5px;background:linear-gradient(#fff,#e9e9e9);display:flex;align-items:center;gap:3px;color:#333}
.social i{display:inline-block;width:9px;height:9px;background:var(--navy-light)}
.intro{left:147px;top:524px;width:600px;font-size:14px;line-height:24px;color:var(--ink)}
.btn-more{left:632px;top:623px;width:78px;height:28px;line-height:26px;border:none;background:linear-gradient(#2d5386,var(--navy-dark));font-size:13px}
.remote-title{left:150px;top:683px}
.remote-list{left:170px;top:724px;list-style:none;font-size:13px;color:var(--muted);line-height:30px}
.relax-photo{left:432px;top:720px;width:285px;height:128px;background:linear-gradient(90deg,#dfe6ee,#b8c4d2 50%,#6b6b6b);border-radius:60px 20px 20px 60px}
.basis{left:155px;top:856px;font-style:italic;font-size:18px;color:var(--navy)}

.contact-title{left:809px;top:496px}
.contact-text{left:808px;top:530px;width:195px;font-size:12px;line-height:14px;color:#111}
.globe{left:1015px;top:490px;width:62px;height:76px;background:radial-gradient(circle at 50% 30%,#7aa7d6,#2b5a8e 60%,transparent 62%)}
.field{left:804px;width:236px;height:38px;border:2px solid #cfcfcf;border-radius:10px;background:linear-gradient(#fff,#f0f0f0);box-shadow:inset 0 2px 4px rgba(0,0,0,.12);font-family:"Montserrat",sans-serif;font-size:13px;color:#333;padding:0 13px;line-height:34px}
.btn-reset{left:867px;top:853px;width:78px;height:28px;line-height:26px;border:none;background:linear-gradient(#2d5386,var(--navy-dark));font-size:13px}
.btn-done{left:960px;top:853px;width:78px;height:28px;line-height:26px;border:none;background:linear-gradient(#2d5386,var(--navy-dark));font-size:13px}
.privacy{left:964px;top:892px;font-size:10px;color:#888}

/* footer */
.site-footer{left:0;top:938px;width:1200px;height:62px;background:#e6e6e6}
.footer-nav{left:129px;top:962px;display:flex;gap:42px;font-family:"Montserrat",sans-serif;font-size:13px;color:#222}
.footer-brand{left:915px;top:954px;display:flex;align-items:center;gap:6px;font-family:"Montserrat",sans-serif;font-weight:600;font-size:26px;color:#6d6d6d;letter-spacing:-.5px}
.footer-brand .dot{width:13px;height:13px;border-radius:50%;background:#6d6d6d}
</style>
</head>
<body>
<header class="abs site-header"></header>
<div class="abs brand"><span class="dot"></span>oloperra</div>
<nav class="abs main-nav"><a class="active">Home</a><a>About us</a><a>Services</a><a>Solutions</a><a>Contact us</a></nav>

<section class="abs hero">
  <div class="abs hero-photo" role="img" aria-label="Smiling businessman in a suit talking on a mobile phone"></div>
  <div class="abs hero-laptop" role="img" aria-label="Open laptop showing a video call"></div>
  <h1 class="abs hero-title">Allowing things to be done</h1>
  <p class="abs hero-sub">without taking time away from more urgent issues<br>or family/personal time.</p>
  <a class="abs btn btn-try">Try it!</a>
  <a class="abs btn btn-buy">Buy it!</a>
  <div class="abs service-tabs">
    <div>Administrative Services</div>
    <div class="active">Technical Services</div>
    <div>Creative Services</div>
  </div>
</section>
<div class="abs hero-band"></div>

<section class="abs panel panel-main"></section>
<h2 class="abs heading help-title">How Can <em>“oloperra.example”</em> Help Me?</h2>
<div class="abs social"><span><i></i>+1</span><span><i></i>Follow</span><span>21k</span><span><i></i>Like</span><span>1</span></div>
<p class="abs intro">By allowing things to be done without taking time away from more urgent issues or family &amp; personal time. Partnering with a VA reduces stress, protects cash flow, eliminates administrative hassles, and enables business people to find the success they originally set out to achieve. Saves small businesses and/or individuals on overhead, salary, etc...</p>
<a class="abs btn btn-more">More...</a>
<h2 class="abs heading remote-title">Work Is done remotely to offer :</h2>
<ul class="abs remote-list">
  <li>Administrative Assistance</li>
  <li>Clerical Service Assistance</li>
  <li>Typing Services Assistance</li>
  <li>Specialist Service Assistance</li>
</ul>
<div class="abs relax-photo" role="img" aria-label="Relaxed businessman leaning back with feet up"></div>
<p class="abs basis">Our services are offered on a regular, ad-hoc or emergency cover basis.</p>

<section class="abs panel panel-contact"></section>
<h2 class="abs heading contact-title">Let us Contact You :</h2>
<p class="abs contact-text">We are all about making your life ea so you just fill in the form below and will contact you...</p>
<div class="abs globe" role="img" aria-label="Globe with two user figures"></div>
<div class="abs field" style="top:599px">Your Fist Name</div>
<div class="abs field" style="top:649px">Your Last Name</div>
<div class="abs field" style="top:699px">Contact Number</div>
<div class="abs field" style="top:749px">E-mail Address</div>
<div class="abs field" style="top:799px">Human Test :&nbsp; 1 + 3 = ?</div>
<a class="abs btn btn-reset">Reset</a>
<a class="abs btn btn-done">Done!</a>
<span class="abs privacy">Privacy Policy</span>

<footer class="abs site-footer"></footer>
<nav class="abs footer-nav"><span>Home</span><span>About us</span><span>Services</span><span>Solutions</span><span>Contact us</span></nav>
<div class="abs footer-brand"><span class="dot"></span>oloperra</div>
</body>
</html>
```